Tarvel Ridge LLC

Need Professional Business cards for New Investment Fund

Target Market(s)

High Quality investors

Industry/Entity Type

Financial

Contact Information for Business Card

Phone Number +1 555 284 6193
Name Pavel Orlinsky
Title Fund Manager
email po@FundTarvel.example
Website www.FundTarvel.example

Colors

Designer to choose colors to be used in the design.

Requirements
Must have
• Must have our Logo and all of the above. Must be made so lettering and loge can be raised

```html
<!DOCTYPE html>
<html lang="en">
<head>
<meta charset="utf-8">
<title>Tarvel Ridge LLC — Business Card</title>
<link rel="stylesheet" href="https://fonts.googleapis.com/css2?family=Didact+Gothic&family=Montserrat:wght@700&display=swap">
<style>
  :root {
    --backdrop: #38393b;
    --card-light: #ffffff;
    --card-dark: #424f42;
    --accent: #58b947;
    --ink-dark: #3d4a3d;
    --ink-light: #ffffff;
  }
  * { box-sizing: border-box; margin: 0; padding: 0; }
  html, body {
    width: 1200px;
    height: 874px;
    overflow: hidden;
    background: var(--backdrop);
    font-family: "Didact Gothic", "Century Gothic", sans-serif;
  }
  .sheet {
    width: 1200px;
    height: 874px;
    display: flex;
    align-items: center;
    justify-content: center;
    gap: 40px;
  }
  .card {
    position: relative;
    width: 540px;
    height: 309px;
    border-radius: 22px;
    border-bottom: 5px solid var(--accent);
    overflow: hidden;
  }
  .card--front { background: var(--card-light); }
  .card--back { background: var(--card-dark); }

  .brand {
    position: absolute;
    display: flex;
    align-items: center;
    gap: 12px;
    font-size: 30px;
    letter-spacing: 1px;
    white-space: nowrap;
  }
  .brand__mark {
    width: 22px;
    height: 22px;
    background: var(--accent);
  }
  .card--front .brand {
    left: 50%;
    top: 50%;
    transform: translate(-50%, -50%);
    color: var(--ink-dark);
  }
  .card--back .brand {
    left: 34px;
    top: 50%;
    transform: translateY(-50%);
    color: var(--ink-light);
    font-size: 26px;
  }

  .divider {
    position: absolute;
    left: 262px;
    top: 70px;
    width: 1px;
    height: 170px;
    background: rgba(255, 255, 255, 0.85);
  }

  .contact {
    position: absolute;
    left: 290px;
    top: 76px;
    color: var(--ink-light);
  }
  .contact__name {
    font-family: "Montserrat", sans-serif;
    font-weight: 700;
    font-size: 19px;
    letter-spacing: 0.5px;
    text-transform: uppercase;
    color: var(--accent);
    line-height: 1.1;
  }
  .contact__title {
    font-size: 15px;
    letter-spacing: 0.5px;
    margin-top: 2px;
  }
  .contact__list {
    list-style: none;
    margin-top: 40px;
    display: flex;
    flex-direction: column;
    gap: 8px;
  }
  .contact__item {
    display: flex;
    align-items: center;
    gap: 10px;
    font-size: 13.5px;
    letter-spacing: 0.3px;
  }
  .contact__icon {
    width: 13px;
    height: 13px;
    flex: none;
  }
</style>
</head>
<body>
  <main class="sheet">
    <section class="card card--front" aria-label="Card front">
      <div class="brand">
        <span class="brand__mark"></span>
        <span class="brand__name">Tarvel Ridge</span>
      </div>
    </section>

    <section class="card card--back" aria-label="Card back">
      <div class="brand">
        <span class="brand__mark"></span>
        <span class="brand__name">Tarvel Ridge</span>
      </div>

      <div class="divider"></div>

      <div class="contact">
        <p class="contact__name">Pavel Orlinsky</p>
        <p class="contact__title">Fund Manager</p>
        <ul class="contact__list">
          <li class="contact__item">
            <svg class="contact__icon" viewBox="0 0 24 24" aria-hidden="true">
              <path fill="#58b947" d="M6.6 10.8a15.1 15.1 0 0 0 6.6 6.6l2.2-2.2a1 1 0 0 1 1-.25 11.4 11.4 0 0 0 3.6.57 1 1 0 0 1 1 1V20a1 1 0 0 1-1 1A17 17 0 0 1 3 4a1 1 0 0 1 1-1h3.5a1 1 0 0 1 1 1c0 1.25.2 2.45.57 3.57a1 1 0 0 1-.25 1z"/>
            </svg>
            <span>+1 555 284 6193</span>
          </li>
          <li class="contact__item">
            <svg class="contact__icon" viewBox="0 0 24 24" aria-hidden="true">
              <rect x="2.5" y="5" width="19" height="14" rx="1.5" fill="none" stroke="#58b947" stroke-width="2"/>
              <path d="M3 6l9 7 9-7" fill="none" stroke="#58b947" stroke-width="2"/>
            </svg>
            <span>po@FundTarvel.example</span>
          </li>
          <li class="contact__item">
            <svg class="contact__icon" viewBox="0 0 24 24" aria-hidden="true">
              <g fill="none" stroke="#58b947" stroke-width="2">
                <circle cx="12" cy="12" r="9.5"/>
                <ellipse cx="12" cy="12" rx="4" ry="9.5"/>
                <path d="M2.5 12h19M4 7h16M4 17h16"/>
              </g>
            </svg>
            <span>www.FundTarvel.example</span>
          </li>
        </ul>
      </div>
    </section>
  </main>
</body>
</html>
```